Real estate business card

I need a business card for my real estate company. I help clients buy and sell properties. I would like to keep the design very simple and professional. I would like the design to convey professionalism, safety and trust. I prefer no graphics but a simple logo design would be nice if that is part of what you do.
Updates

Please keep the designs simple. No high-rise buildings please. 

Reason: My design has not been finalized.

Target Market(s)

Age group 30-60 mostly affluent

Industry/Entity Type

Real Estate

Contact Information for Business Card

Velmont Realtors
Howard Prisk, Broker
4153 Marlow Ave. #226, La Crescenta, CA 91207

Requirements
Nice to have
• Logo can be combination of my initials HP or just Z or a simple geometric shape? Please see "Desig Ideas" attachment. No pics of houses or shaking hands, dollar bills, $, %, etc...
Please use fonts similar to Helvetica for a clean, modern look (think Northern European design, simple, clean yet bold)

Also use font colors such as blue, grey in different shades. Use pastel colors if better.

```html
<!DOCTYPE html>
<html lang="en">
<head>
<meta charset="utf-8">
<title>Velmont Realtors – Business Card</title>
<link rel="stylesheet" href="https://fonts.googleapis.com/css2?family=Inter:wght@300;400&display=swap">
<style>
  :root {
    --backdrop: #101416;
    --card-dark: #3a3a3a;
    --card-mid: #5c5c5c;
    --card-light: #7a7a7a;
    --blue-deep: #1780f0;
    --blue-bright: #3fb2ff;
    --blue-pale: #8fe3ff;
    --rim: #e6e6e6;
    --text-main: #ffffff;
    --text-soft: #d9d9d9;
  }
  html, body {
    margin: 0;
    width: 1200px;
    height: 1164px;
    overflow: hidden;
    background: var(--backdrop);
    font-family: "Inter", Helvetica, Arial, sans-serif;
  }
  .card {
    position: absolute;
    left: 100px;
    top: 296px;
    width: 1000px;
    height: 572px;
    overflow: hidden;
    background: radial-gradient(circle at 52% 42%, var(--card-light) 0%, var(--card-mid) 30%, var(--card-dark) 80%);
    box-shadow: 0 10px 30px rgba(0,0,0,0.6);
  }
  .card-shapes {
    position: absolute;
    inset: 0;
  }
  .brand {
    position: absolute;
    left: 64px;
    top: 140px;
    display: flex;
    align-items: center;
    gap: 18px;
    color: var(--text-main);
    font-weight: 300;
    font-size: 44px;
    letter-spacing: 0.5px;
    line-height: 1.1;
  }
  .brand-square {
    flex: none;
    width: 60px;
    height: 60px;
    border: 3px solid var(--text-main);
    box-sizing: border-box;
  }
  .brand-name span { display: block; }
  .details {
    position: absolute;
    right: 60px;
    top: 60px;
    text-align: right;
    color: var(--text-main);
    font-weight: 300;
  }
  .details p { margin: 0; }
  .company { font-size: 42px; margin-bottom: 22px !important; }
  .person { font-size: 34px; margin-bottom: 6px !important; }
  .title { font-size: 30px; color: var(--text-soft); margin-bottom: 52px !important; }
  .phone { font-size: 30px; margin-bottom: 62px !important; letter-spacing: 0.5px; }
  .address { font-size: 30px; line-height: 1.35; font-style: normal; margin: 0; }
  .license {
    position: absolute;
    left: 80px;
    bottom: 40px;
    color: var(--text-main);
    font-weight: 300;
    font-size: 28px;
    margin: 0;
    letter-spacing: 0.5px;
  }
</style>
</head>
<body>
  <main class="card">
    <svg class="card-shapes" width="1000" height="572" viewBox="0 0 1000 572" aria-hidden="true">
      <defs>
        <radialGradient id="blue-disc" cx="0.3" cy="0.35" r="0.75">
          <stop offset="0" stop-color="#8fe3ff"/>
          <stop offset="0.45" stop-color="#3fb2ff"/>
          <stop offset="1" stop-color="#1780f0"/>
        </radialGradient>
      </defs>
      <circle class="soft-circle" cx="810" cy="270" r="240" fill="#ffffff" fill-opacity="0.06"/>
      <circle class="soft-circle" cx="300" cy="600" r="200" fill="#ffffff" fill-opacity="0.06"/>
      <circle class="disc-rim" cx="206" cy="128" r="312" fill="#e6e6e6"/>
      <circle class="disc" cx="198" cy="120" r="310" fill="url(#blue-disc)"/>
    </svg>

    <div class="brand">
      <span class="brand-square"></span>
      <span class="brand-name"><span>Velmont</span><span>Real Estate</span></span>
    </div>

    <section class="details">
      <p class="company">Velmont Realtors</p>
      <p class="person">Howard Prisk</p>
      <p class="title">Broker</p>
      <p class="phone">(818) 555-0147</p>
      <address class="address">4153 Marlow Ave. #226,<br>La Crescenta, CA 91207</address>
    </section>

    <p class="license">CA BRE 01458833</p>
  </main>
</body>
</html>
```